Verdant Vitality Healthcare Practitioner Multivitamin Detailing Brochure

We need a healthcare practitioner detailing brochure for a company based in Pretoria South Africa. The brochure is used to educate healthcare practitioners and persuade them to prescribe Verdant Vitality Multivitamin in their daily practice. Find attached all the necessary text required in the brochure. We would like a 4 paged A4 sized brochure (i.e. A3 folded). We would like to see designs that use the same colour orange to match the supplement bottle and our funky modern brand look. I have attached our supplement design, content etc. The final design should communicate professionalism, confidence and encourage healthcare practitioners to prescribe the product.

```html
<!DOCTYPE html>
<html lang="en">
<head>
<meta charset="utf-8">
<title>Verdant Vitality Multivitamin Brochure</title>
<link rel="stylesheet" href="https://fonts.googleapis.com/css2?family=Open+Sans:wght@300;400;600&display=swap">
<style>
  :root {
    --canvas: #e8e8e8;
    --paper: #ffffff;
    --orange: #e58e2b;
    --grey-light: #f2f2f2;
    --grey-dark: #a6a6a6;
    --green: #14b04a;
    --green-soft: #7dd6a0;
    --blue: #1c9dd9;
    --title-grey: #8a8a8a;
    --brand: #2b63ad;
  }
  html, body {
    margin: 0;
    width: 936px;
    height: 1200px;
    overflow: hidden;
    background: var(--canvas);
    font-family: "Open Sans", sans-serif;
  }
  .page {
    position: absolute;
    left: 188px;
    width: 560px;
    height: 560px;
    display: block;
    background: var(--paper);
  }
  .page--front { top: 25px; }
  .page--back { top: 615px; }
  .brand-name { font-family: "Open Sans", sans-serif; font-weight: 600; fill: var(--brand); }
  .brand-dot { fill: var(--brand); }
  .cover-title { font-weight: 300; fill: var(--title-grey); }
  .nutrient { fill: var(--green); }
  .nutrient-dot { fill: var(--green-soft); }
  .nutrient-label { font-weight: 400; fill: #fff; text-anchor: middle; }
  .feature-circle { fill: var(--blue); }
  .feature-text { font-weight: 300; fill: #fff; text-anchor: middle; }
  .contact-footer { font-weight: 400; fill: #fff; font-size: 7px; }
  .contact-block { font-weight: 400; fill: var(--title-grey); font-size: 10px; text-anchor: middle; letter-spacing: 0.5px; }
  .band-orange { fill: var(--orange); }
</style>
</head>
<body>

<svg class="page page--front" viewBox="0 0 660 660" xmlns="http://www.w3.org/2000/svg">
  <defs>
    <linearGradient id="greyBand" x1="0" x2="1" y1="0" y2="0">
      <stop offset="0" stop-color="#f4f4f4"/>
      <stop offset="1" stop-color="#9c9c9c"/>
    </linearGradient>
    <linearGradient id="arcGrey" x1="0" x2="1" y1="0" y2="1">
      <stop offset="0" stop-color="#ffffff"/>
      <stop offset="0.5" stop-color="#a8a8a8"/>
      <stop offset="1" stop-color="#ffffff"/>
    </linearGradient>
    <linearGradient id="bottleBody" x1="0" x2="1" y1="0" y2="0">
      <stop offset="0" stop-color="#c9731c"/>
      <stop offset="0.5" stop-color="#ec9a3e"/>
      <stop offset="1" stop-color="#c46d18"/>
    </linearGradient>
    <linearGradient id="bottleCap" x1="0" x2="1" y1="0" y2="0">
      <stop offset="0" stop-color="#e6e6e6"/>
      <stop offset="0.5" stop-color="#ffffff"/>
      <stop offset="1" stop-color="#dcdcdc"/>
    </linearGradient>
  </defs>

  <rect class="band-top" x="0" y="0" width="660" height="130" fill="url(#greyBand)"/>
  <path class="band-orange" d="M0,30 Q130,22 260,25 C180,25 80,40 0,72 Z"/>
  <path fill="#fff" d="M0,72 C80,40 180,25 260,25 C420,25 560,60 660,100 L660,660 L0,660 Z"/>

  <path class="band-bottom" d="M0,600 C220,585 450,540 660,485 L660,660 L0,660 Z" fill="url(#greyBand)"/>

  <circle class="nutrient-field" cx="250" cy="455" r="225" fill="#fff" stroke="#ececec" stroke-width="1.5"/>
  <path d="M180,240 C290,205 400,260 425,335" fill="none" stroke="url(#arcGrey)" stroke-width="10" stroke-linecap="round"/>

  <path class="band-orange" d="M0,610 C220,600 450,575 660,560 L660,660 L0,660 Z"/>

  <circle class="brand-dot" cx="250" cy="90" r="13"/>
  <text class="brand-name" x="270" y="99" font-size="26">Verdant Vitality</text>

  <text class="cover-title" x="330" y="188" font-size="52" text-anchor="middle">VERDANT VITALITY</text>
  <text class="cover-title" x="335" y="238" font-size="29" text-anchor="middle">MULTIVITAMIN</text>

  <circle class="nutrient" cx="150" cy="347" r="51"/>
  <text class="nutrient-label" x="150" y="362" font-size="42">Mg</text>
  <circle class="nutrient" cx="83" cy="428" r="45"/>
  <text class="nutrient-label" x="83" y="440" font-size="32">Se</text>
  <circle class="nutrient" cx="106" cy="528" r="40"/>
  <text class="nutrient-label" x="106" y="539" font-size="29">B6</text>
  <circle class="nutrient" cx="188" cy="580" r="34"/>
  <text class="nutrient-label" x="188" y="589" font-size="25">Ca</text>
  <circle class="nutrient" cx="282" cy="570" r="30"/>
  <text class="nutrient-label" x="282" y="579" font-size="24">Co</text>
  <circle class="nutrient-dot" cx="327" cy="503" r="15"/>

  <circle class="feature-circle" cx="291" cy="394" r="78"/>
  <text class="feature-text" x="291" y="378" font-size="54">5in1</text>
  <text class="feature-text" x="291" y="400" font-size="15">Multivitamin</text>
  <text class="feature-text" x="291" y="419" font-size="15">Antioxidant</text>
  <text class="feature-text" x="291" y="438" font-size="15">Amino acid</text>
  <text class="feature-text" x="291" y="457" font-size="15">Mineral</text>

  <g role="img" aria-label="Product photograph: white multivitamin bottle with orange label">
    <rect x="408" y="272" width="165" height="65" rx="10" fill="url(#bottleCap)"/>
    <rect x="393" y="330" width="195" height="308" rx="22" fill="#f3f3f3"/>
    <rect x="393" y="400" width="195" height="190" fill="url(#bottleBody)"/>
  </g>

  <circle cx="27" cy="626" r="7" fill="#fff"/>
  <text class="contact-footer" x="40" y="624">INFO@VERDANTVITALITY.CO.ZA | TEL: 012 555 0184 |</text>
  <text class="contact-footer" x="40" y="635">WWW.VERDANTVITALITY.CO.ZA</text>
</svg>

<svg class="page page--back" viewBox="0 0 660 660" xmlns="http://www.w3.org/2000/svg">
  <defs>
    <linearGradient id="greyBandBack" x1="0" x2="1" y1="0" y2="0">
      <stop offset="0" stop-color="#f4f4f4"/>
      <stop offset="1" stop-color="#9c9c9c"/>
    </linearGradient>
    <linearGradient id="arcGreyBack" x1="0" x2="0" y1="0" y2="1">
      <stop offset="0" stop-color="#ffffff"/>
      <stop offset="0.5" stop-color="#a0a0a0"/>
      <stop offset="1" stop-color="#ffffff"/>
    </linearGradient>
  </defs>

  <rect x="0" y="0" width="660" height="130" fill="url(#greyBandBack)"/>
  <path class="band-orange" d="M0,30 Q130,22 260,25 C180,25 80,40 0,72 Z"/>
  <path fill="#fff" d="M0,72 C80,40 180,25 260,25 C420,25 560,60 660,100 L660,660 L0,660 Z"/>

  <path d="M0,600 C220,585 450,540 660,485 L660,660 L0,660 Z" fill="url(#greyBandBack)"/>
  <path class="band-orange" d="M0,610 C220,600 450,575 660,560 L660,660 L0,660 Z"/>

  <circle cx="330" cy="347" r="127" fill="#fff" stroke="#ececec" stroke-width="1.5"/>
  <path d="M340,222 C420,225 470,300 455,375 C445,425 410,460 370,470" fill="none" stroke="url(#arcGreyBack)" stroke-width="9" stroke-linecap="round"/>

  <circle class="brand-dot" cx="254" cy="318" r="12"/>
  <text class="brand-name" x="272" y="326" font-size="23">Verdant Vitality</text>

  <text class="contact-block" x="330" y="386">INFO@VERDANTVITALITY.CO.ZA</text>
  <text class="contact-block" x="330" y="402">TEL: 012 555 0184</text>
  <text class="contact-block" x="330" y="418">WWW.VERDANTVITALITY.CO.ZA</text>
</svg>

</body>
</html>
```